Custom Home Builder Needs a Website

Harbor Pine Builders Ltd. requires a clean professional 5 page website - Home, About Us, Gallery (Interior and Exterior), Our Process and Contact Us(with registration form). We are a home builder who also has homes for sale. Also please have a place for video embedding. Editable fields by user. Using the stationery 'feel' that is attached. Need social media links. If you require any additional files, please request.

Target Market(s)

Families and professionals

Industry/Entity Type

Home Builder

Coding

Coded - Design and coding required

Number of Pages Required

5+ page

Font styles to use
Sans Serif
Other font styles liked:
• Lato

Requirements
Must have
• Editable by user
• Register Button
• Place to put home models for sale - preferably on the first page
• 5 page website -
• -Home
• -About Us
• -Gallery (Interior and Exterior)
• -Our Process
• -Contact Us.
Nice to have
• Themed similar to current stationery
• place for video embedding
• Try some darker backgrounds
• Change pictures to B/W if works for design
Should not have
• cartoonish type of content

```html
<!DOCTYPE html>
<html lang="en">
<head>
<meta charset="utf-8">
<title>Harbor Pine Builders Ltd.</title>
<link href="https://fonts.googleapis.com/css2?family=Roboto+Condensed:wght@400;700&family=Lato:wght@400;700&display=swap" rel="stylesheet">
<style>
:root{
  --green:#5c9a4b;
  --green-dark:#4a8239;
  --green-soft:rgba(92,154,75,.55);
  --ink:#2a2a2a;
  --dark:#2b2b2b;
  --darker:#1e1e1e;
  --footer:#232323;
  --bar:#161616;
  --card:#ebebeb;
  --muted:#666;
  --light:#d8d8d8;
  --white:#fff;
}
*{box-sizing:border-box;margin:0;padding:0}
html,body{width:1200px;height:3383px;overflow:hidden}
body{position:relative;background:var(--dark);font-family:"Lato",sans-serif;color:var(--white)}
.abs{position:absolute}

/* hero */
.hero{left:0;top:0;width:1200px;height:600px;background:linear-gradient(180deg,#b7c6d2 0%,#8e8f88 35%,#6d6255 60%,#8a8b7f 80%,#6c8a4a 100%)}
.logo-box{left:160px;top:16px;width:208px;height:88px;background:var(--white);display:flex;align-items:center;justify-content:center;gap:8px;padding:0 10px}
.logo-box .mark{width:14px;height:14px;background:var(--green);flex:none}
.logo-box .name{font-family:"Roboto Condensed",sans-serif;font-weight:700;color:var(--green);font-size:17px;line-height:1.1}
.contact-strip{left:690px;top:16px;width:350px;height:52px;background:var(--white);display:flex;align-items:center;justify-content:space-around;font-size:10px;color:var(--ink)}
.contact-item{display:flex;align-items:center;gap:8px;line-height:1.25}
.contact-item .dot{width:26px;height:26px;border-radius:50%;background:var(--green);display:flex;align-items:center;justify-content:center}
.nav{left:379px;top:68px;height:38px;display:flex;background:var(--green)}
.nav a{font-family:"Roboto Condensed",sans-serif;font-size:11px;color:var(--white);text-decoration:none;padding:0 14px;display:flex;align-items:center;letter-spacing:.3px}
.nav a.active{background:var(--green-dark)}
.nav a.register{background:#555}
.nav-tail{left:936px;top:68px;width:104px;height:38px;background:var(--white);display:flex;align-items:center;justify-content:center;gap:6px}
.nav-tail span{width:18px;height:18px;border-radius:50%;border:1.5px solid var(--green)}
.side-tab{top:316px;width:24px;height:80px;background:var(--green-soft);display:flex;align-items:center;justify-content:center;font-family:"Roboto Condensed",sans-serif;font-size:9px;writing-mode:vertical-rl;letter-spacing:2px}
.hero-title{left:350px;top:293px;width:500px;height:52px;border-radius:26px;background:rgba(130,130,130,.85);font-family:"Roboto Condensed",sans-serif;font-weight:700;font-size:29px;display:flex;align-items:center;justify-content:center}
.hero-sub{left:388px;top:359px;width:424px;height:52px;border-radius:26px;background:rgba(110,110,110,.85);font-size:11px;text-align:center;display:flex;align-items:center;justify-content:center;line-height:1.5}
.btn{height:38px;width:138px;border-radius:19px;font-family:"Roboto Condensed",sans-serif;font-weight:700;font-size:11px;display:flex;align-items:center;justify-content:center;gap:10px}
.btn-green{background:var(--green);color:var(--white)}
.btn-white{background:var(--white);color:var(--green)}
.btn i{width:12px;height:12px;border-radius:50%;display:flex;align-items:center;justify-content:center}
.btn-green i{background:var(--white)}
.btn-white i{background:var(--green)}

/* search */
.search{left:0;top:600px;width:1200px;height:205px;background:var(--green)}
.search h2{position:absolute;left:0;width:1200px;top:14px;text-align:center;font-family:"Roboto Condensed",sans-serif;font-size:22px;font-weight:700}
.field{width:280px;height:34px;border:1px solid rgba(255,255,255,.45);border-radius:17px;font-family:"Roboto Condensed",sans-serif;font-size:11px;display:flex;align-items:center;justify-content:space-between;padding:0 16px}

/* about */
.about-img{left:160px;top:848px;width:429px;height:305px;background:linear-gradient(180deg,#c9d3dc 0%,#b7b0a4 45%,#8a7d6f 70%,#6f8a4d 100%)}
.about-img .frame{position:absolute;left:40px;top:28px;width:370px;height:250px;border:1px solid rgba(255,255,255,.8)}
.about-text{left:611px;top:858px;width:430px}
.eyebrow{font-family:"Roboto Condensed",sans-serif;font-size:12px;color:var(--green);font-weight:700}
.about-text h3{font-family:"Roboto Condensed",sans-serif;font-size:20px;margin:2px 0 12px}
.about-text p{font-size:11px;line-height:1.55;color:var(--light);margin-bottom:12px}

/* video */
.video{left:0;top:1195px;width:1200px;height:452px;background:linear-gradient(100deg,#3b2a20 0%,#6b4a35 30%,#c9bba6 50%,#5a3e2c 75%,#2d211a 100%)}
.play{left:578px;top:1390px}

/* section titles */
.sec-title{left:0;width:1200px;text-align:center;font-family:"Roboto Condensed",sans-serif;font-weight:700;font-size:19px;color:var(--green);letter-spacing:.5px}
.sec-icon{left:586px}

/* cards */
.card{width:280px;height:311px;background:var(--card);color:var(--ink)}
.card .photo{height:185px}
.card .head{display:flex;justify-content:space-between;padding:12px 10px 6px;font-family:"Roboto Condensed",sans-serif;font-weight:700;font-size:14px}
.card .head b{color:var(--green)}
.card p{padding:0 10px;font-size:10px;line-height:1.5;color:var(--muted)}
.card .addr{display:flex;align-items:center;gap:8px;padding:10px 10px 0;font-size:10px;color:var(--muted)}

/* gallery */
.tile{position:absolute}
.tile.feature::after{content:"";position:absolute;inset:0;background:rgba(92,154,75,.75)}
.plus{left:355px;top:2635px;z-index:2}

/* footer */
.footer{left:0;top:3035px;width:1200px;height:294px;background:var(--footer)}
.foot-col{top:3077px;width:260px}
.foot-col h4{font-family:"Roboto Condensed",sans-serif;font-size:12px;color:var(--green);margin-bottom:28px}
.foot-col p{font-size:10px;line-height:1.55;color:#cfcfcf}
.foot-logo{display:flex;align-items:center;gap:6px;font-family:"Roboto Condensed",sans-serif;font-weight:700;font-size:14px;color:#bbb;margin-bottom:18px}
.foot-logo span{width:10px;height:10px;background:#bbb}
.touch{display:flex;gap:10px;font-size:10px;color:#cfcfcf;margin-bottom:24px;line-height:1.5}
.input{width:200px;height:27px;border:1px solid #888;border-radius:4px;font-size:10px;color:#aaa;padding:6px 8px;margin-top:10px}
.input.tall{height:59px}
.send{margin-top:12px;width:62px;height:22px;border-radius:11px;background:var(--green);font-size:9px;font-family:"Roboto Condensed",sans-serif;font-weight:700;display:flex;align-items:center;justify-content:center}
.copyright{left:0;top:3329px;width:1200px;height:54px;background:var(--bar);font-size:10px;color:#ccc;display:flex;align-items:center;justify-content:center}
</style>
</head>
<body>

<!-- Hero -->
<div class="abs hero" role="img" aria-label="Photograph of a craftsman style family home with stone and timber facade and a landscaped front yard"></div>
<div class="abs logo-box"><span class="mark"></span><span class="name">Harbor Pine Builders Ltd.</span></div>
<div class="abs contact-strip">
  <div class="contact-item"><span class="dot"><svg width="12" height="12" viewBox="0 0 24 24"><path fill="#fff" d="M6.6 10.8a15 15 0 0 0 6.6 6.6l2.2-2.2c.3-.3.7-.4 1-.2 1.1.4 2.3.6 3.6.6.6 0 1 .4 1 1V20c0 .6-.4 1-1 1A17 17 0 0 1 3 4c0-.6.4-1 1-1h3.5c.6 0 1 .4 1 1 0 1.3.2 2.5.6 3.6.1.3 0 .7-.2 1z"/></svg></span><span>You can call us<br><b>555-014-2290</b></span></div>
  <div class="contact-item"><span class="dot"><svg width="12" height="12" viewBox="0 0 24 24"><path fill="#fff" d="M3 5h18v14H3z"/><path d="M3 5l9 7 9-7" fill="none" stroke="#5c9a4b" stroke-width="2"/></svg></span><span>You can mail us<br><b>hello@harborpinebuilders.ca</b></span></div>
</div>
<nav class="abs nav">
  <a class="active">HOME</a><a>ABOUT US</a><a>GALLERY</a><a>OUR PROCESS</a><a>CONTACT US</a><a class="register">REGISTER</a>
</nav>
<div class="abs nav-tail"><span></span><span></span><span></span></div>
<div class="abs side-tab" style="left:40px">PREV</div>
<div class="abs side-tab" style="left:1136px">NEXT</div>
<div class="abs hero-title">THE BEST WAY TO FIND YOUR HOME</div>
<div class="abs hero-sub">Lorem consectetur adipiscing elit, sed do eiusmod tempor<br>dolor sit ametconsetetur adipiscing elit, sed do eiusmod tempor incididunt</div>
<div class="abs btn btn-green" style="left:531px;top:424px">READ MORE <i><svg width="6" height="6" viewBox="0 0 6 6"><path d="M1 0l4 3-4 3z" fill="#5c9a4b"/></svg></i></div>

<!-- Search -->
<section class="abs search">
  <h2>FIND YOUR HOME HERE</h2>
</section>
<div class="abs field" style="left:160px;top:662px">LOCATION <span>&#8964;</span></div>
<div class="abs field" style="left:460px;top:662px">MIN AREA <span>&#8964;</span></div>
<div class="abs field" style="left:760px;top:662px">MAX AREA <span>&#8964;</span></div>
<div class="abs field" style="left:160px;top:706px">NUMBER OF BADROOM <span>&#8964;</span></div>
<div class="abs field" style="left:460px;top:706px">NUMBER OF BATHROOM <span>&#8964;</span></div>
<div class="abs field" style="left:760px;top:706px">YOUR BUDGET <span>&#8964;</span></div>
<div class="abs btn btn-white" style="left:531px;top:753px">READ MORE <i><svg width="6" height="6" viewBox="0 0 6 6"><path d="M1 0l4 3-4 3z" fill="#fff"/></svg></i></div>

<!-- About -->
<div class="abs about-img" role="img" aria-label="Photograph of a two storey stone and siding show home with a double garage"><div class="frame"></div></div>
<div class="abs about-text">
  <div class="eyebrow">ABOUT</div>
  <h3>HARBOR PINE BUILDERS</h3>
  <p>Lorem Ipsum is simply dummy text of the printing and typesetting industry. Lorem Ipsum has been the industry's standard dummy text ever since the 1500s, when an unknown printer took a galley of type and scrambled it to make a type specimen book.</p>
  <p>It has survived not only five centuries, but also the leap into electronic typesetting, remaining essentially unchanged. It was popularised in the 1960s with the release of Typeleaf sheets containing Lorem Ipsum passages, and more recently with desktop publishing software like Pagecraft Studio including versions of Lorem Ipsum.</p>
  <p>Lorem Ipsum is simply dummy text of the printing and typesetting industry. Lorem Ipsum has been the industry's standard dummy text ever since the 1500s, when an unknown printer took a galley of type and scrambled it to make a type specimen book.</p>
</div>

<!-- Video -->
<div class="abs video" role="img" aria-label="Video still of a blurred kitchen interior with dark wood cabinets and a window"></div>
<svg class="abs play" width="40" height="40" viewBox="0 0 40 40"><circle cx="20" cy="20" r="18" fill="none" stroke="#fff" stroke-width="2"/><path d="M16 12l12 8-12 8z" fill="#fff"/></svg>

<!-- Featured -->
<svg class="abs sec-icon" style="top:1680px" width="28" height="22" viewBox="0 0 28 22"><g fill="#777"><rect x="2" y="10" width="5" height="12"/><rect x="9" y="3" width="6" height="19"/><rect x="17" y="7" width="5" height="15"/><rect x="24" y="13" width="3" height="9"/></g></svg>
<div class="abs sec-title" style="top:1706px">FEATURED PROPERTY</div>

<div class="abs card" style="left:160px;top:1764px"><div class="photo" role="img" aria-label="Photograph of a bright kitchen with island and pendant lights" style="background:linear-gradient(135deg,#e9e4dc,#a9958a 60%,#4a3a30)"></div><div class="head">MASONS DE VILLA <b>$52,350</b></div><p>Dolor sit amet, conse ctetur adipiscing elit, sed do eiusmod tempor incididunt ut labore et lorea aliquant minim veniam, quis nostrud</p><div class="addr"><svg width="9" height="12" viewBox="0 0 9 12"><path d="M4.5 0A4.5 4.5 0 0 0 0 4.5C0 8 4.5 12 4.5 12S9 8 9 4.5A4.5 4.5 0 0 0 4.5 0z" fill="#666"/><circle cx="4.5" cy="4.5" r="1.6" fill="#ebebeb"/></svg>PO Box 214 Lakeview, SK, S0K 2B1</div></div>
<div class="abs card" style="left:460px;top:1764px"><div class="photo" role="img" aria-label="Photograph of a gas range with a red kettle and mosaic backsplash" style="background:linear-gradient(135deg,#9a8f86,#6e655f 50%,#2f2b2a)"></div><div class="head">MASONS DE VILLA <b>$52,350</b></div><p>Dolor sit amet, conse ctetur adipiscing elit, sed do eiusmod tempor incididunt ut labore et lorea aliquant minim veniam, quis nostrud</p><div class="addr"><svg width="9" height="12" viewBox="0 0 9 12"><path d="M4.5 0A4.5 4.5 0 0 0 0 4.5C0 8 4.5 12 4.5 12S9 8 9 4.5A4.5 4.5 0 0 0 4.5 0z" fill="#666"/><circle cx="4.5" cy="4.5" r="1.6" fill="#ebebeb"/></svg>PO Box 214 Lakeview, SK, S0K 2B1</div></div>
<div class="abs card" style="left:760px;top:1764px"><div class="photo" role="img" aria-label="Photograph of a home office with a dark wood desk and panelled walls" style="background:linear-gradient(135deg,#f0eeea,#d6d2cb 60%,#4b2e22)"></div><div class="head">MASONS DE VILLA <b>$52,350</b></div><p>Dolor sit amet, conse ctetur adipiscing elit, sed do eiusmod tempor incididunt ut labore et lorea aliquant minim veniam, quis nostrud</p><div class="addr"><svg width="9" height="12" viewBox="0 0 9 12"><path d="M4.5 0A4.5 4.5 0 0 0 0 4.5C0 8 4.5 12 4.5 12S9 8 9 4.5A4.5 4.5 0 0 0 4.5 0z" fill="#666"/><circle cx="4.5" cy="4.5" r="1.6" fill="#ebebeb"/></svg>PO Box 214 Lakeview, SK, S0K 2B1</div></div>
<div class="abs card" style="left:160px;top:2103px"><div class="photo" role="img" aria-label="Photograph of a child's bedroom with a single bed and soft pastel tones" style="background:linear-gradient(135deg,#e8f0f2,#c7d2d8 55%,#d9a7c4)"></div><div class="head">MASONS DE VILLA <b>$52,350</b></div><p>Dolor sit amet, conse ctetur adipiscing elit, sed do eiusmod tempor incididunt ut labore et lorea aliquant minim veniam, quis nostrud</p><div class="addr"><svg width="9" height="12" viewBox="0 0 9 12"><path d="M4.5 0A4.5 4.5 0 0 0 0 4.5C0 8 4.5 12 4.5 12S9 8 9 4.5A4.5 4.5 0 0 0 4.5 0z" fill="#666"/><circle cx="4.5" cy="4.5" r="1.6" fill="#ebebeb"/></svg>PO Box 214 Lakeview, SK, S0K 2B1</div></div>
<div class="abs card" style="left:460px;top:2103px"><div class="photo" role="img" aria-label="Photograph of a dark roofed bungalow with a paved driveway" style="background:linear-gradient(180deg,#bcd0e2,#6e6a66 55%,#8a8478)"></div><div class="head">MASONS DE VILLA <b>$52,350</b></div><p>Dolor sit amet, conse ctetur adipiscing elit, sed do eiusmod tempor incididunt ut labore et lorea aliquant minim veniam, quis nostrud</p><div class="addr"><svg width="9" height="12" viewBox="0 0 9 12"><path d="M4.5 0A4.5 4.5 0 0 0 0 4.5C0 8 4.5 12 4.5 12S9 8 9 4.5A4.5 4.5 0 0 0 4.5 0z" fill="#666"/><circle cx="4.5" cy="4.5" r="1.6" fill="#ebebeb"/></svg>PO Box 214 Lakeview, SK, S0K 2B1</div></div>
<div class="abs card" style="left:760px;top:2103px"><div class="photo" role="img" aria-label="Photograph of a stone front home with a green lawn" style="background:linear-gradient(180deg,#e6ecef,#7d7a74 55%,#6f9a4a)"></div><div class="head">MASONS DE VILLA <b>$52,350</b></div><p>Dolor sit amet, conse ctetur adipiscing elit, sed do eiusmod tempor incididunt ut labore et lorea aliquant minim veniam, quis nostrud</p><div class="addr"><svg width="9" height="12" viewBox="0 0 9 12"><path d="M4.5 0A4.5 4.5 0 0 0 0 4.5C0 8 4.5 12 4.5 12S9 8 9 4.5A4.5 4.5 0 0 0 4.5 0z" fill="#666"/><circle cx="4.5" cy="4.5" r="1.6" fill="#ebebeb"/></svg>PO Box 214 Lakeview, SK, S0K 2B1</div></div>

<!-- Gallery -->
<svg class="abs sec-icon" style="top:2453px" width="28" height="22" viewBox="0 0 28 22"><g fill="#777"><rect x="2" y="10" width="5" height="12"/><rect x="9" y="3" width="6" height="19"/><rect x="17" y="7" width="5" height="15"/><rect x="24" y="13" width="3" height="9"/></g></svg>
<div class="abs sec-title" style="top:2479px">OUR GALLERY</div>

<div class="tile feature" role="img" aria-label="Photograph of a stone and siding family home exterior" style="left:160px;top:2540px;width:429px;height:230px;background:linear-gradient(180deg,#dfe6ea,#8b857c 55%,#6e8f4b)"></div>
<svg class="abs plus" width="36" height="36" viewBox="0 0 36 36"><circle cx="18" cy="18" r="16" fill="none" stroke="#fff" stroke-width="2"/><path d="M18 11v14M11 18h14" stroke="#fff" stroke-width="2"/></svg>
<div class="tile" role="img" aria-label="Photograph of a kitchen range with a red kettle" style="left:611px;top:2540px;width:203px;height:230px;background:linear-gradient(135deg,#a59a8e,#6a625c 55%,#3a3532)"></div>
<div class="tile" role="img" aria-label="Photograph of a white kitchen with pendant lights" style="left:837px;top:2540px;width:203px;height:230px;background:linear-gradient(135deg,#f2eee8,#b9a897 55%,#5a4436)"></div>
<div class="tile" role="img" aria-label="Photograph of a home office with a dark desk" style="left:160px;top:2795px;width:203px;height:230px;background:linear-gradient(135deg,#eeebe6,#cfcac2 60%,#4b2e22)"></div>
<div class="tile" role="img" aria-label="Photograph of a bathroom vanity with pendant lights" style="left:386px;top:2795px;width:203px;height:230px;background:linear-gradient(135deg,#e7e3dc,#b8aea3 55%,#6b5a4c)"></div>
<div class="tile" role="img" aria-label="Photograph of a stone front family home with a lawn" style="left:611px;top:2795px;width:429px;height:230px;background:linear-gradient(180deg,#e8eef1,#7f7b75 55%,#6c984a)"></div>

<!-- Footer -->
<footer class="abs footer"></footer>
<div class="abs foot-col" style="left:160px">
  <h4>ABOUT US</h4>
  <div class="foot-logo"><span></span>Harbor Pine Builders</div>
  <p>Lorem ipsum dolor sit amet, consectetur adipiscing elit. Nunc in dictum enim. Sed eu urna metus. Aenean et orci lorem. Vivamus blandit augue at nulla dignissim, quis porttitor nulla iaculis. Ut et porta leo, a ultricies sem. Morbi at elementum diam, sit amet vehicula tellus.</p>
</div>
<div class="abs foot-col" style="left:460px">
  <h4>GET IN TOUCH</h4>
  <div class="touch"><svg width="10" height="13" viewBox="0 0 9 12"><path d="M4.5 0A4.5 4.5 0 0 0 0 4.5C0 8 4.5 12 4.5 12S9 8 9 4.5A4.5 4.5 0 0 0 4.5 0z" fill="#aaa"/></svg><span>PO Box 214 Lakeview,<br>SK, S0K 2B1</span></div>
  <div class="touch"><svg width="11" height="11" viewBox="0 0 24 24"><path fill="#aaa" d="M6.6 10.8a15 15 0 0 0 6.6 6.6l2.2-2.2c.3-.3.7-.4 1-.2 1.1.4 2.3.6 3.6.6.6 0 1 .4 1 1V20c0 .6-.4 1-1 1A17 17 0 0 1 3 4c0-.6.4-1 1-1h3.5c.6 0 1 .4 1 1 0 1.3.2 2.5.6 3.6.1.3 0 .7-.2 1z"/></svg><span>555-014-2290</span></div>
  <div class="touch"><svg width="12" height="10" viewBox="0 0 24 20"><rect x="1" y="1" width="22" height="18" fill="none" stroke="#aaa" stroke-width="2"/><path d="M1 1l11 9 11-9" fill="none" stroke="#aaa" stroke-width="2"/></svg><span>hello@harborpinebuilders.ca</span></div>
</div>
<div class="abs foot-col" style="left:760px">
  <h4>QUICK CONTACT</h4>
  <p style="margin-top:-14px">Lorem ipsum dolor sit amet, consectetur<br>adipiscing elit.</p>
  <div class="input">Type your email</div>
  <div class="input tall">Message</div>
  <div class="send">SEND</div>
</div>
<div class="abs copyright">Copyright © 2016 Harbor Pine Builders. All rights reserved.</div>

</body>
</html>
```